Business Card Design

redesign of card and recreation of logo based on image provided. the business is located in new york so the Brooklyn Bridge figures prominently in the scheme. product should be very clean.

Industry/Entity Type

Real Estate

Contact Information for Business Card

Wendell Ortwick 318 Tamsin Street Brooklyn, New York 11409 wendell@qorvane.com Mobile: 917-555-0143

Colors
cadf82
1b1b1b
ffffff

Requirements
Nice to have
• Brooklyn Bridge

```html
<!DOCTYPE html>
<html lang="en">
<head>
<meta charset="utf-8">
<title>Qorvane Realty — Business Card</title>
<link rel="stylesheet" href="https://fonts.googleapis.com/css2?family=Cormorant+Garamond:wght@500;600&family=Lato:wght@400;700&display=swap">
<style>
  :root {
    --lime: #cadf82;
    --ink: #1b1b1b;
    --paper: #ffffff;
    --band: #3a3b3c;
    --band-shade: #6b6c6d;
    --back: #2a2b2d;
    --stage: #e6e8ea;
    --sketch-dark: #9a9c9e;
    --sketch-light: #f1f2f2;
  }
  * { box-sizing: border-box; margin: 0; padding: 0; }
  html, body { width: 934px; height: 1200px; overflow: hidden; }
  body {
    background: var(--stage);
    position: relative;
    font-family: "Lato", sans-serif;
  }
  .card {
    position: absolute;
    left: 87px;
    width: 760px;
    height: 434px;
    overflow: hidden;
    box-shadow: 0 6px 18px rgba(0,0,0,0.12);
  }
  .card--front { top: 110px; background: var(--paper); }
  .card--back { top: 656px; background: var(--back); }

  .brand-name {
    position: absolute;
    text-align: center;
    font-family: "Cormorant Garamond", serif;
    font-weight: 500;
    line-height: 1;
    white-space: nowrap;
  }
  .card--front .brand-name {
    left: 350px; top: 48px; width: 380px;
    font-size: 36px;
    color: var(--ink);
  }
  .card--back .brand-name {
    left: 120px; top: 150px; width: 520px;
    font-size: 46px;
    color: var(--paper);
  }

  .holder { position: absolute; left: 350px; top: 108px; width: 380px; text-align: center; }
  .holder__name {
    font-family: "Cormorant Garamond", serif;
    font-weight: 600;
    font-size: 19px;
    text-transform: uppercase;
    color: var(--ink);
  }
  .holder__title {
    font-size: 8px;
    font-weight: 700;
    letter-spacing: 1px;
    text-transform: uppercase;
    color: var(--ink);
  }

  .skyline-art {
    position: absolute;
    left: 0; top: 150px;
    width: 760px; height: 170px;
    background: linear-gradient(90deg, var(--sketch-light) 0%, var(--sketch-dark) 35%, #c9cbcc 70%, var(--sketch-light) 100%);
    opacity: 0.75;
  }

  .contact-band {
    position: absolute;
    left: 30px; right: 30px; top: 300px;
    height: 78px;
    background: var(--band);
    border-bottom: 10px solid var(--band-shade);
    display: flex;
    align-items: center;
    justify-content: space-between;
    padding: 0 28px;
    color: var(--paper);
    font-size: 13px;
    line-height: 1.35;
  }
  .contact { display: flex; align-items: center; gap: 14px; }
  .contact__icon { width: 22px; height: 22px; fill: var(--lime); flex: none; }
  .contact--web { font-size: 11.5px; }

  .back-stripe {
    position: absolute;
    left: 40px; right: 0; top: 340px;
    height: 5px;
    background: var(--lime);
  }
</style>
</head>
<body>

<section class="card card--front" aria-label="Card front">
  <div class="skyline-art" role="img" aria-label="Pencil sketch of a suspension bridge over the river with the city skyline"></div>

  <div class="brand-name">Qorvane Realty</div>

  <div class="holder">
    <div class="holder__name">Wendell Ortwick</div>
    <div class="holder__title">Broker</div>
  </div>

  <div class="contact-band">
    <div class="contact">
      <svg class="contact__icon" viewBox="0 0 24 24" aria-hidden="true"><path d="M12 3 2 12h3v9h5v-6h4v6h5v-9h3z"/></svg>
      <div>318 Tamsin Street<br>Brooklyn, New York 11409</div>
    </div>
    <div class="contact">
      <svg class="contact__icon" viewBox="0 0 24 24" aria-hidden="true"><path d="M6.6 10.8a15.1 15.1 0 0 0 6.6 6.6l2.2-2.2a1 1 0 0 1 1-.25 11.4 11.4 0 0 0 3.6.57 1 1 0 0 1 1 1V20a1 1 0 0 1-1 1A17 17 0 0 1 3 4a1 1 0 0 1 1-1h3.5a1 1 0 0 1 1 1c0 1.250.2 2.45.57 3.6a1 1 0 0 1-.25 1z"/></svg>
      <div>T: 917-555-0143<br>F: 917-555-0178</div>
    </div>
    <div class="contact contact--web">
      <svg class="contact__icon" viewBox="0 0 24 24" aria-hidden="true"><path d="M12 2a10 10 0 1 0 0 20 10 10 0 0 0 0-20zm0 2c.9 1.2 1.6 2.6 2 4h-4c.4-1.4 1.1-2.8 2-4zM4.3 14a8 8 0 0 1 0-4h3.4a16 16 0 0 0 0 4zm.8 2h3c.3 1.3.8 2.6 1.5 3.7A8 8 0 0 1 5.1 16zm3-8h-3a8 8 0 0 1 4.5-3.7C8.9 5.4 8.4 6.7 8.1 8zM12 20c-.9-1.2-1.6-2.6-2-4h4c-.4 1.4-1.1 2.8-2 4zm2.3-6H9.7a14 14 0 0 1 0-4h4.6a14 14 0 0 1 0 4zm.1 5.7c.7-1.1 1.2-2.4 1.5-3.7h3a8 8 0 0 1-4.5 3.7zM16.3 14a16 16 0 0 0 0-4h3.4a8 8 0 0 1 0 4zm-.4-6c-.3-1.3-.8-2.6-1.5-3.7A8 8 0 0 1 18.9 8z"/></svg>
      <div>wendell@qorvane.com<br>www.qorvane.com</div>
    </div>
  </div>
</section>

<section class="card card--back" aria-label="Card back">
  <div class="brand-name">Qorvane Realty</div>
  <div class="back-stripe"></div>
</section>

</body>
</html>
```